Run Specialty Brick & Mortar and Ecom site

We use shopify POS and have a crappy shopify webpage. We want to update our webpage to improve the landing page, add a store, add a blog area
you can look at www.copperfinchstride.com to see what we have and
www.saltmeadowpace.com and www.quillhops.com to see what we want.

```html
<!DOCTYPE html>
<html lang="en">
<head>
<meta charset="utf-8">
<title>Copperfinch Stride</title>
<link href="https://fonts.googleapis.com/css2?family=Montserrat:wght@400;500;600;700&display=swap" rel="stylesheet">
<style>
:root{
  --navy:#1f1d4a;
  --ink:#23244f;
  --text:#3a3a48;
  --muted:#8a8a96;
  --accent:#6d8bca;
  --card:#d3dff2;
  --strip:#e7edf8;
  --tint:#eef1f7;
  --white:#ffffff;
}
*{margin:0;padding:0;box-sizing:border-box}
html,body{width:1200px;height:3939px;overflow:hidden;background:var(--white)}
body{font-family:'Montserrat',sans-serif;color:var(--text);position:relative}
.abs{position:absolute}
.topbar{left:0;top:0;width:1200px;height:32px;background:var(--navy);color:var(--white);font-size:12px;font-weight:500;text-align:center;line-height:32px}
.brand{left:107px;top:38px;width:92px;height:92px;border-radius:50%;border:2px solid var(--navy);display:flex;align-items:center;justify-content:center;text-align:center;font-size:11px;font-weight:600;color:var(--navy);line-height:1.2}
.search{left:382px;top:53px;width:418px;height:34px;border:1px solid #c9ccd6;border-radius:6px;overflow:hidden}
.search span{position:absolute;left:18px;top:9px;font-size:11px;color:#888}
.search .go{position:absolute;right:0;top:0;width:88px;height:34px;background:var(--accent);display:flex;align-items:center;justify-content:center}
.nav{top:110px;font-size:14px;color:#555}
.nav.active{color:var(--navy);font-weight:700}
.nav-bar{left:286px;top:142px;width:46px;height:5px;background:var(--accent)}
.badge{left:1070px;top:52px;width:16px;height:16px;border-radius:50%;background:var(--accent);color:#fff;font-size:10px;text-align:center;line-height:16px}
.hero{left:0;top:147px;width:1200px;height:454px;background:linear-gradient(100deg,#9a5c45 0%,#b0725a 45%,#8b8f86 70%,#6fa4a8 100%)}
.hero-title{left:112px;top:233px;font-size:40px;font-weight:600;color:#fff;line-height:52.5px;letter-spacing:.5px}
.btn{background:var(--accent);color:#fff;border-radius:5px;font-size:15px;font-weight:500;display:flex;align-items:center;justify-content:center}
.eyebrow{left:0;width:1200px;text-align:center;font-size:21px;color:var(--ink);letter-spacing:.3px}
.heading{left:0;width:1200px;text-align:center;font-size:35px;font-weight:700;color:var(--ink)}
.cat{top:803px;width:299px;height:315px;background:var(--card)}
.cat .strip{position:absolute;left:0;top:0;width:50px;height:315px;background:var(--strip)}
.cat .label{position:absolute;left:10px;bottom:22px;writing-mode:vertical-rl;transform:rotate(180deg);font-size:22px;font-weight:500;color:var(--ink);letter-spacing:.5px}
.cat .art{position:absolute;left:80px;top:80px;width:200px;height:200px;border-radius:20px;background:radial-gradient(circle,#4f6fc0 0%,rgba(79,111,192,0) 70%)}
.arrow{width:35px;height:35px;border-radius:50%;border:1.5px solid var(--ink);display:flex;align-items:center;justify-content:center}
.prod{top:1402px;width:226px;height:173px;background:#e4ebf7}
.prod .art{position:absolute;left:28px;top:30px;width:170px;height:110px;border-radius:50%;background:radial-gradient(ellipse,#6f7a88 0%,rgba(111,122,136,0) 70%)}
.price{top:1600px;font-size:14px;color:var(--text)}
.pname{top:1624px;width:235px;font-size:16px;font-weight:500;color:#1f1f2a;line-height:23px}
.pbrand{top:1674px;font-size:15px;color:var(--muted)}
.banner{left:0;top:1850px;width:1200px;height:374px;background:linear-gradient(90deg,#a06a48 0%,#6a4a36 35%,#3a322e 60%,#2f2b2a 100%)}
.banner-text{right:112px;text-align:right;color:#fff}
.about-label{left:112px;top:2305px;font-size:21px;color:var(--ink)}
.about-title{left:112px;top:2340px;font-size:36px;font-weight:600;color:var(--ink);line-height:43px}
.para{left:110px;width:470px;font-size:15px;line-height:23px;color:#4a4a55}
.photo{left:649px;top:2362px;width:392px;height:392px;border-radius:50%;background:#fff;box-shadow:0 6px 18px rgba(0,0,0,.18)}
.photo .inner{position:absolute;left:14px;top:14px;width:364px;height:364px;border-radius:50%;background:linear-gradient(160deg,#7c8fa6,#2f4c7d 60%,#1f2d4a)}
.flowers{left:985px;top:2340px;width:125px;height:200px;border-radius:60px;background:linear-gradient(180deg,#3c5bb0,#6b86d6 70%,#8aa25c)}
.blogbg{left:0;top:2859px;width:1200px;height:734px;background:var(--tint)}
.post{top:3076px;width:299px;height:364px;background:#fff;box-shadow:0 2px 10px rgba(0,0,0,.08)}
.post .img{position:absolute;left:0;top:0;width:299px;height:202px}
.post .meta{position:absolute;left:16px;top:221px;font-size:10px;color:#777;display:flex;gap:10px;align-items:center}
.post .rule{position:absolute;left:16px;right:16px;top:243px;height:1px;background:#e2e2e8}
.post .title{position:absolute;left:16px;top:262px;width:270px;font-size:16px;font-weight:500;color:#1f1f2a;line-height:23px}
.post .more{position:absolute;left:16px;top:323px;font-size:14px;color:var(--ink);text-decoration:underline}
.footer{left:0;top:3593px;width:1200px;height:346px;background:var(--navy);color:#fff}
.flogo{left:110px;top:3676px;width:140px;height:140px;border-radius:50%;background:#fff;display:flex;align-items:center;justify-content:center;text-align:center;font-size:15px;font-weight:600;color:var(--navy);line-height:1.25}
.fcol{top:3641px;color:#fff}
.fcol h4{font-size:19px;font-weight:600;margin-bottom:18px}
.fcol li{list-style:none;font-size:15px;line-height:27.5px;color:#e4e6f3}
.frule{left:110px;top:3877px;width:980px;height:1px;background:#7e80a8}
.copy{left:0;top:3893px;width:1200px;text-align:center;font-size:14px;color:#fff}
</style>
</head>
<body>

<div class="abs topbar">Welcome! We invite you to visit us for all your running needs provided with personal service by local owners!</div>

<header>
  <div class="abs brand">Copperfinch<br>Stride</div>
  <div class="abs search"><span>Search</span><div class="go"><svg width="16" height="16" viewBox="0 0 16 16"><circle cx="6.5" cy="6.5" r="5" fill="none" stroke="#fff" stroke-width="2"/><line x1="10.5" y1="10.5" x2="15" y2="15" stroke="#fff" stroke-width="2"/></svg></div></div>
  <svg class="abs" style="left:1011px;top:57px" width="28" height="24" viewBox="0 0 28 24"><path d="M14 22 C4 14 1 10 3 5 C5 1 11 1 14 6 C17 1 23 1 25 5 C27 10 24 14 14 22Z" fill="none" stroke="#222" stroke-width="2"/></svg>
  <svg class="abs" style="left:1050px;top:58px" width="26" height="24" viewBox="0 0 26 24"><path d="M2 2h4l3 14h13l2-10H8" fill="none" stroke="#222" stroke-width="2"/><circle cx="11" cy="21" r="1.8" fill="#222"/><circle cx="20" cy="21" r="1.8" fill="#222"/></svg>
  <div class="abs badge">0</div>
  <nav>
    <span class="abs nav active" style="left:286px">Home</span>
    <span class="abs nav" style="left:359px">About Us</span>
    <span class="abs nav" style="left:451px">Shoes</span>
    <span class="abs nav" style="left:521px">Apparel &amp; Socks</span>
    <span class="abs nav" style="left:660px">Electronics</span>
    <span class="abs nav" style="left:764px">Nutrition</span>
    <span class="abs nav" style="left:856px">Accessories</span>
    <span class="abs nav" style="left:963px">Gift Cards</span>
    <span class="abs nav" style="left:1059px">Blog</span>
  </nav>
  <div class="abs nav-bar"></div>
</header>

<section>
  <div class="abs hero" role="img" aria-label="Runner tying a turquoise running shoe on a red track"></div>
  <div class="abs hero-title">WALKING, RUNNING,<br>EVERYTHING IN BETWEEN.<br>PERSONAL SERVICE WITH<br>A SMILE</div>
  <div class="abs btn" style="left:112px;top:466px;width:131px;height:34px">Shop Now</div>
</section>

<section>
  <div class="abs eyebrow" style="top:684px">EXPLORE OUR STORE</div>
  <div class="abs heading" style="top:718px">INNOVATION &amp; CONFORT</div>
  <div class="abs cat" style="left:110px;background:#7290cf;box-shadow:0 3px 10px rgba(0,0,0,.25)"><div class="strip"></div><div class="label">SHOES</div><div class="art" role="img" aria-label="Pair of white and red running sneakers"></div></div>
  <div class="abs cat" style="left:451px"><div class="strip"></div><div class="label">APPAREL &amp; SOCKS</div><div class="art" role="img" aria-label="Pair of blue athletic socks"></div></div>
  <div class="abs cat" style="left:790px"><div class="strip"></div><div class="label">NUTRITION</div><div class="art" role="img" aria-label="Supplement bottle with yellow capsules" style="background:radial-gradient(circle,#f4f4f4 0%,#e0c050 45%,rgba(224,192,80,0) 72%)"></div></div>
  <div class="abs arrow" style="left:555px;top:1157px"><svg width="10" height="12" viewBox="0 0 10 12"><path d="M7 1L2 6l5 5" fill="none" stroke="#23244f" stroke-width="2"/></svg></div>
  <div class="abs arrow" style="left:610px;top:1157px"><svg width="10" height="12" viewBox="0 0 10 12"><path d="M3 1l5 5-5 5" fill="none" stroke="#23244f" stroke-width="2"/></svg></div>
</section>

<section>
  <div class="abs eyebrow" style="top:1275px">THE LATEST TRENDS IN ATHLETIC FOOTWEAR</div>
  <div class="abs heading" style="top:1310px">SNEAKERS &amp; KICKS</div>

  <div class="abs prod" style="left:110px"><div class="art" role="img" aria-label="Grey and sage running sneaker"></div></div>
  <div class="abs prod" style="left:361px"><div class="art" role="img" aria-label="Navy suede sneaker"></div></div>
  <div class="abs prod" style="left:613px"><div class="art" role="img" aria-label="Black knit training shoe"></div></div>
  <div class="abs prod" style="left:864px"><div class="art" role="img" aria-label="White and blue running shoe"></div></div>

  <div class="abs price" style="left:110px">$25.00</div>
  <div class="abs price" style="left:361px">$25.00</div>
  <div class="abs price" style="left:613px">$25.00</div>
  <div class="abs price" style="left:864px">$25.00</div>
  <div class="abs pname" style="left:110px">Lorem ipsum dolor sit am consectetur adipis</div>
  <div class="abs pname" style="left:361px">Lorem ipsum dolor sit am consectetur adipis</div>
  <div class="abs pname" style="left:613px">Lorem ipsum dolor sit am consectetur adipis</div>
  <div class="abs pname" style="left:864px">Lorem ipsum dolor sit am consectetur adipis</div>
  <div class="abs pbrand" style="left:110px">StrideLane</div>
  <div class="abs pbrand" style="left:361px">StrideLane</div>
  <div class="abs pbrand" style="left:613px">StrideLane</div>
  <div class="abs pbrand" style="left:864px">StrideLane</div>

  <div class="abs btn" style="left:534px;top:1727px;width:131px;height:34px">View More</div>
</section>

<section>
  <div class="abs banner" role="img" aria-label="Hands fastening an orange-strapped sports smartwatch"></div>
  <div class="abs banner-text" style="top:1944px;font-size:20px">Electronics</div>
  <div class="abs banner-text" style="top:1990px;font-size:35px;font-weight:500;line-height:42px">Performance-Packed<br>Smartwatch for Athletes</div>
  <div class="abs btn" style="left:957px;top:2090px;width:130px;height:34px">Shop Now</div>
</section>

<section>
  <div class="abs about-label">About Us</div>
  <div class="abs about-title">The Perfect Product for<br>Every Pace</div>
  <p class="abs para" style="top:2452px">While Mara was born in the area, Tomas got here as fast as he could (when he was 13). They met in the 80's, got married in the 90's and just celebrated 30 years together.&nbsp; Tomas played for the Harbor Gulls (nothing impressive, just minor leagues) and we lived all over our great country.&nbsp; After being away from the Greater Lakeside Area, we moved back in mid-2024 and settled near Route 9 &amp; Elm, so we are definitely local!</p>
  <p class="abs para" style="top:2629px">We're both active. Mara plays tennis and Tomas tries to complete (not very quickly mind you) a full-distance triathlon each year. Our daughter is a veterinary student and our son a nuclear engineering major.</p>
  <div class="abs btn" style="left:110px;top:2741px;width:132px;height:34px">Learn More</div>
  <div class="abs photo"><div class="inner" role="img" aria-label="The two owners smiling together at a running event"></div></div>
  <div class="abs flowers" role="img" aria-label="Sprigs of blue wildflowers"></div>
</section>

<section>
  <div class="abs blogbg"></div>
  <div class="abs eyebrow" style="top:2943px">LATEST BLOG</div>
  <div class="abs heading" style="top:2978px">BEST GEAR FOR WALKING, RUNNING</div>

  <article class="abs post" style="left:110px">
    <div class="img" role="img" aria-label="Runner in a red shirt jogging outdoors" style="background:linear-gradient(135deg,#5d7a2e,#b8352e 60%,#3b4a22)"></div>
    <div class="meta"><span style="color:#c65">&#9675; By Admin</span><span style="color:#c65">&#9675; 0 Comments</span></div>
    <div class="rule"></div>
    <div class="title">Lorem ipsum dolor sit amet, co sectetur adipi</div>
    <div class="more">Read More</div>
  </article>
  <article class="abs post" style="left:451px">
    <div class="img" role="img" aria-label="Hands lacing red running shoes" style="background:linear-gradient(135deg,#3b6a70,#c8453c 55%,#2b4f55)"></div>
    <div class="meta"><span style="color:#c65">&#9675; By Admin</span><span style="color:#c65">&#9675; 0 Comments</span></div>
    <div class="rule"></div>
    <div class="title">Lorem ipsum dolor sit amet, co sectetur adipi</div>
    <div class="more">Read More</div>
  </article>
  <article class="abs post" style="left:790px">
    <div class="img" role="img" aria-label="Orange and white supplement capsule" style="background:linear-gradient(135deg,#3a1a14,#d8552a 50%,#1e1412)"></div>
    <div class="meta"><span style="color:#c65">&#9675; By Admin</span><span style="color:#c65">&#9675; 0 Comments</span></div>
    <div class="rule"></div>
    <div class="title">Lorem ipsum dolor sit amet, co sectetur adipi</div>
    <div class="more">Read More</div>
  </article>

  <div class="abs arrow" style="left:555px;top:3473px"><svg width="10" height="12" viewBox="0 0 10 12"><path d="M7 1L2 6l5 5" fill="none" stroke="#23244f" stroke-width="2"/></svg></div>
  <div class="abs arrow" style="left:610px;top:3473px"><svg width="10" height="12" viewBox="0 0 10 12"><path d="M3 1l5 5-5 5" fill="none" stroke="#23244f" stroke-width="2"/></svg></div>
</section>

<footer>
  <div class="abs footer"></div>
  <div class="abs flogo">Copperfinch<br>Stride</div>
  <div class="abs fcol" style="left:313px"><h4>Help &amp; Information</h4><ul><li>Custom Service</li><li>F.A.Q.'s</li><li>Ordering Tracking</li><li>Contact Us</li><li>Events</li><li>Popular</li></ul></div>
  <div class="abs fcol" style="left:558px"><h4>About us</h4><ul><li>About Us</li><li>Delivery Information</li><li>Privacy Policy</li><li>Discount</li><li>Custom Service</li><li>Term &amp; Condition</li></ul></div>
  <div class="abs fcol" style="left:777px"><h4>Company</h4><ul><li>Sitemap</li><li>Privacy Policy</li><li>Your Account</li><li>Advanced Search</li><li>Term &amp; Condition</li><li>Contact Us</li></ul></div>
  <div class="abs fcol" style="left:971px"><h4>Categories</h4><ul><li>Shoes</li><li>Apparel &amp; Socks</li><li>Electronics</li><li>Nutrition</li><li>Accessories</li><li>Gift Cards</li></ul></div>
  <div class="abs frule"></div>
  <div class="abs copy">Copyright © 2025 Copperfinch Stride. All rights reserved.</div>
</footer>

</body>
</html>
```